Bref créative
Contract folder, Biz Card,Letter head, Fax Cov, Env,A4 Env,CD Cov&Pack,PPT
Email Sign, scratch paper
Professional
Harvinder Pal Okoro
Director
Vel Metrics Systems Private Limited
Plot No. 217 Industrial Growth Zone Phase 4 Distt- Kelmar 174 398, Punjab, India
hokoro@velmetrics.example
www.VelMetrics.example
on letter head & envelops we would prefer to mention the manufacturers we represent on Letter Head, Biz Card, A4 Env.
1) Brovane Instruments 2) Tollwick Fendor 3) Mo-Ve-Sel 4) Dovin
5) TUVO 6) Plazor 7) Orvix 8) Universal Prism Workshops 9) KV Fabrications 10) Tolbry Chemical 11) MaxiSp 12) DOR Scientific 13) VextaMol 14) KPL
1) use only logo
2) write official email info@velmetrics.example & website www.VelMetrics.example
3) Write in small "Suppliers of Chromatography Consumables & Spectroscopy Supplies"
WE ARE OPEN TO IDEAS
Vel Metrics System Private Limited Logo
vms id card sample content
logo eps format

```html
<!DOCTYPE html>
<html lang="en">
<head>
<meta charset="utf-8">
<title>VelMetrics Business Card Presentation</title>
<link rel="stylesheet" href="https://fonts.googleapis.com/css2?family=Cinzel:wght@400&family=Arimo:wght@400;700&display=swap">
<style>
  :root {
    --page: #ffffff;
    --label: #6b6b6b;
    --ink: #3a3a3a;
    --name-blue: #2a7fc4;
    --rule-blue: #2a7fc4;
    --blue-light: #2f86d4;
    --blue-dark: #0b3f86;
    --grey-light: #b4b4b4;
    --grey-dark: #6a6a6a;
    --red-light: #ee2a2a;
    --red-dark: #9e0c10;
    --white: #ffffff;
  }
  * { box-sizing: border-box; margin: 0; padding: 0; }
  html, body { width: 1200px; height: 857px; overflow: hidden; background: var(--page); }
  body { position: relative; font-family: "Arimo", Arial, sans-serif; }

  .side-label {
    position: absolute;
    width: 540px;
    text-align: center;
    font-family: "Cinzel", "Times New Roman", serif;
    font-size: 30px;
    letter-spacing: 2px;
    color: var(--label);
  }

  .card {
    position: absolute;
    width: 540px;
    height: 300px;
    overflow: hidden;
    box-shadow: 0 10px 14px -6px rgba(0,0,0,0.35);
  }
  .pos-tl { left: 48px;  top: 100px; }
  .pos-tr { left: 612px; top: 100px; }
  .pos-bl { left: 48px;  top: 478px; }
  .pos-br { left: 612px; top: 478px; }

  /* Front */
  .card-front { background: var(--white); border: 1px solid #e4e4e4; }
  .front-brand {
    position: absolute; left: 30px; top: 56px;
    font-size: 26px; font-weight: 400; color: var(--ink); line-height: 1;
  }
  .holder { position: absolute; left: 270px; top: 152px; }
  .holder-name { font-size: 16px; color: var(--name-blue); }
  .holder-title { font-size: 11px; color: var(--ink); margin-top: 4px; }
  .accent-bar { position: absolute; left: 0; top: 174px; width: 8px; height: 72px; background: var(--rule-blue); }
  .contact { position: absolute; left: 22px; top: 176px; font-size: 10.5px; line-height: 1.45; color: var(--ink); }

  /* Backs */
  .card-back { color: var(--white); }
  .back-blue { background: radial-gradient(ellipse at 55% 45%, var(--blue-light), var(--blue-dark)); }
  .back-grey { background: radial-gradient(ellipse at 55% 45%, var(--grey-light), var(--grey-dark)); }
  .back-red  { background: radial-gradient(ellipse at 55% 45%, var(--red-light), var(--red-dark)); }
  .principals {
    position: absolute; top: 18px; left: 0; width: 100%;
    text-align: center; font-size: 11.5px; line-height: 1.5;
  }
  .back-brand {
    position: absolute; left: 0; width: 100%; top: 150px;
    text-align: center; font-size: 18px; font-weight: 400; color: var(--white); line-height: 1;
  }
  .tagline { position: absolute; left: 20px; bottom: 22px; font-size: 11px; line-height: 1.35; }
  .web { position: absolute; right: 22px; bottom: 22px; font-size: 10.5px; }
</style>
</head>
<body>

  <div class="side-label" style="left:48px; top:48px;">FRONT</div>
  <div class="side-label" style="left:612px; top:48px;">BACK</div>
  <div class="side-label" style="left:48px; top:426px;">BACK</div>
  <div class="side-label" style="left:612px; top:426px;">BACK</div>

  <section class="card card-front pos-tl">
    <div class="front-brand">Vel Metrics System</div>
    <div class="holder">
      <div class="holder-name">Harvinder Pal Okoro</div>
      <div class="holder-title">Director</div>
    </div>
    <div class="accent-bar"></div>
    <div class="contact">
      Plot No. 217 Industrial Growth Zone Phase 4<br>
      Distt- Kelmar 174 398, Punjab, India<br>
      P: 0184-4417260, 4417261, 6092483<br>
      C: +91 90412 73806 &nbsp;F: 0184-4417299<br>
      E: hokoro@velmetrics.example<br>
      www.VelMetrics.example
    </div>
  </section>

  <section class="card card-back back-blue pos-tr">
    <div class="principals">
      Brovane Instruments | Tollwick Fendor | Mo-Ve-Sel | Dovin<br>
      TUVO | Plazor | Orvix | Universal Prism Workshops<br>
      KV Fabrications | Tolbry Chemical | MaxiSp | DOR Scientific<br>
      VextaMol | KPL
    </div>
    <div class="back-brand">Vel Metrics System</div>
    <div class="tagline">Suppliers of Chromatography Consumables<br>&amp; Spectroscopy Supplies</div>
    <div class="web">www.VelMetrics.example</div>
  </section>

  <section class="card card-back back-grey pos-bl">
    <div class="principals">
      Brovane Instruments | Tollwick Fendor | Mo-Ve-Sel | Dovin<br>
      TUVO | Plazor | Orvix | Universal Prism Workshops<br>
      KV Fabrications | Tolbry Chemical | MaxiSp | DOR Scientific<br>
      VextaMol | KPL
    </div>
    <div class="back-brand">Vel Metrics System</div>
    <div class="tagline">Suppliers of Chromatography Consumables<br>&amp; Spectroscopy Supplies</div>
    <div class="web">www.VelMetrics.example</div>
  </section>

  <section class="card card-back back-red pos-br">
    <div class="principals">
      Brovane Instruments | Tollwick Fendor | Mo-Ve-Sel | Dovin<br>
      TUVO | Plazor | Orvix | Universal Prism Workshops<br>
      KV Fabrications | Tolbry Chemical | MaxiSp | DOR Scientific<br>
      VextaMol | KPL
    </div>
    <div class="back-brand">Vel Metrics System</div>
    <div class="tagline">Suppliers of Chromatography Consumables<br>&amp; Spectroscopy Supplies</div>
    <div class="web">www.VelMetrics.example</div>
  </section>

</body>
</html>
```